Psychologist needs a Sign & Postcard Design

I need the attached text & pictures to be arranged in a professional & impactful way so that people waiting to see other practitioners will notice my sign & walk away with the postcard (which matches the sign). Possibly the pictures of smiling people could be arranged on either side of the list called " Psychological Strategies for". The banner size is 830mm x 2000mm (Deskmart Retractable Exhibition Banner). The postcard size is DL 99 x 210mm (Printello). I'd like it set up so that the resolution works well for both individual print jobs. Also, I'd like the pictures to be sized well for each individual print job i.e. the format should be the same for both print jobs but if the scaled down version for the postcard means the pictures/text are too small then I would need it to be set up differently to make it readable & well presented. I like a collage style of picture arrangement. I'd rather the pictures weren't too large, but were still recognisable. I also have chosen a background colour which I think may be suitable. Please use the fonts I've used in the Info attachment. I would like the logo (my name & title etc) left as is. The final design should communicate a professional service & be positive.

```html
<!DOCTYPE html>
<html lang="en">
<head>
<meta charset="utf-8">
<title>Daniel McAllister – Clinical Psychologist Banner</title>
<link href="https://fonts.googleapis.com/css2?family=Tinos:wght@400;700&family=Arimo:wght@400;700&display=swap" rel="stylesheet">
<style>
  :root {
    --brand-blue: #1f4f9c;
    --brand-navy: #17335f;
    --sky-top: #ffffff;
    --sky-bottom: #dbe8f6;
    --photo-a: #c9b39a;
    --photo-b: #8fb0d3;
    --white: #ffffff;
  }
  * { margin: 0; padding: 0; box-sizing: border-box; }
  html, body { width: 889px; height: 1200px; overflow: hidden; }
  body {
    background: #eef1f5;
    font-family: "Arimo", Arial, sans-serif;
  }
  .banner {
    width: 889px; height: 1200px;
    display: flex; flex-direction: column;
    background: linear-gradient(180deg, var(--sky-top) 0%, var(--sky-top) 40%, var(--sky-bottom) 100%);
  }
  .web-bar {
    flex: 0 0 46px; background: var(--brand-blue); color: var(--white);
    display: flex; align-items: center; justify-content: center;
    font-size: 22px; letter-spacing: 0.5px;
  }
  .identity { flex: 0 0 auto; text-align: center; color: var(--brand-blue); padding-top: 20px; }
  .identity__name {
    font-family: "Tinos", "Times New Roman", serif; font-weight: 400;
    font-size: 64px; line-height: 0.98; letter-spacing: 1px;
  }
  .identity__title {
    font-family: "Tinos", "Times New Roman", serif;
    font-size: 22px; letter-spacing: 7px; margin-top: 10px;
  }
  .identity__credentials { font-size: 12px; line-height: 1.35; margin-top: 6px; color: var(--brand-navy); }
  .collage {
    flex: 0 0 auto;
    margin: 18px 60px 0; padding: 8px; background: var(--brand-blue);
    display: grid; grid-template-columns: repeat(6, 1fr); grid-template-rows: repeat(3, 60px); gap: 6px;
  }
  .collage__photo { background: linear-gradient(135deg, var(--photo-a), var(--photo-b)); }
  .collage__photo:nth-child(3n) { background: linear-gradient(135deg, #e0cdb7, #b9c9d9); }
  .collage__photo:nth-child(4n+1) { background: linear-gradient(135deg, #a9c4de, #d9c2a8); }
  .strategies { flex: 1 1 auto; min-height: 0; text-align: center; color: var(--brand-navy); padding-top: 20px; }
  .strategies__heading { font-weight: 700; font-size: 20px; letter-spacing: 0.5px; color: var(--brand-blue); margin-bottom: 10px; }
  .strategies__list { list-style: none; font-size: 16px; line-height: 18.5px; }
  .contact-bar {
    flex: 0 0 92px; background: var(--brand-blue); color: var(--white);
    text-align: center; display: flex; flex-direction: column; justify-content: center; gap: 4px;
    font-size: 16px;
  }
  .contact-bar__phone { display: inline-flex; align-items: center; justify-content: center; gap: 6px; font-weight: 700; }
  .contact-bar__hours { font-size: 14px; }
</style>
</head>
<body>
<main class="banner">
  <header class="web-bar">www.calmpathpsychology.com.au</header>

  <section class="identity">
    <h1 class="identity__name">DANIEL<br>McALLISTER</h1>
    <p class="identity__title">CLINICAL PSYCHOLOGIST</p>
    <p class="identity__credentials">MPsych., Member National Psychology Society,<br>Member College of Clinical Psychologists</p>
  </section>

  <section class="collage">
    <div class="collage__photo" role="img" aria-label="Photo of a smiling man"></div>
    <div class="collage__photo" role="img" aria-label="Photo of a smiling couple"></div>
    <div class="collage__photo" role="img" aria-label="Photo of a happy family"></div>
    <div class="collage__photo" role="img" aria-label="Photo of a smiling woman"></div>
    <div class="collage__photo" role="img" aria-label="Photo of a smiling teenager"></div>
    <div class="collage__photo" role="img" aria-label="Photo of a smiling older man"></div>
    <div class="collage__photo" role="img" aria-label="Photo of a smiling child"></div>
    <div class="collage__photo" role="img" aria-label="Photo of friends laughing"></div>
    <div class="collage__photo" role="img" aria-label="Photo of a smiling young woman"></div>
    <div class="collage__photo" role="img" aria-label="Photo of a smiling mother and baby"></div>
    <div class="collage__photo" role="img" aria-label="Photo of a smiling older woman"></div>
    <div class="collage__photo" role="img" aria-label="Photo of a smiling student"></div>
    <div class="collage__photo" role="img" aria-label="Photo of a smiling businessman"></div>
    <div class="collage__photo" role="img" aria-label="Photo of a group of smiling people"></div>
    <div class="collage__photo" role="img" aria-label="Photo of a smiling girl"></div>
    <div class="collage__photo" role="img" aria-label="Photo of a smiling senior couple"></div>
    <div class="collage__photo" role="img" aria-label="Photo of a smiling young man"></div>
    <div class="collage__photo" role="img" aria-label="Photo of a smiling woman outdoors"></div>
  </section>

  <section class="strategies">
    <h2 class="strategies__heading">PSYCHOLOGICAL STRATEGIES FOR:</h2>
    <ul class="strategies__list">
      <li>Anxiety &amp; Worry</li>
      <li>Depression</li>
      <li>Sleep Difficulties</li>
      <li>Relationship Problems</li>
      <li>Panic</li>
      <li>Stress</li>
      <li>Burnout</li>
      <li>Overcoming Procrastination</li>
      <li>Achieving Life Goals</li>
      <li>Dealing with Difficult Personalities</li>
      <li>Anger</li>
      <li>Legal Concerns</li>
      <li>Obsessive Compulsive Behaviours</li>
      <li>Self Esteem Problems</li>
      <li>Trauma/Post Traumatic Stress</li>
      <li>Social Anxiety</li>
      <li>Confidence Building</li>
      <li>Phobias</li>
      <li>Assertiveness</li>
      <li>Body Image Issues</li>
      <li>Mood Problems</li>
      <li>Identity Difficulties</li>
      <li>Bipolar Disorder</li>
      <li>Post Natal Depression</li>
      <li>Grief &amp; Loss</li>
      <li>Coping with Life Change</li>
      <li>Overcoming Childhood Trauma</li>
      <li>Relaxation</li>
    </ul>
  </section>

  <footer class="contact-bar">
    <p class="contact-bar__address">Elmwood Superclinic, Ground Floor, 12 Harbour Lane, Westvale</p>
    <p class="contact-bar__phone">
      <svg width="16" height="16" viewBox="0 0 24 24" aria-hidden="true"><path fill="#ffffff" d="M6.6 10.8a15.1 15.1 0 0 0 6.6 6.6l2.2-2.2a1 1 0 0 1 1-.25 11.4 11.4 0 0 0 3.6.57 1 1 0 0 1 1 1V20a1 1 0 0 1-1 1A17 17 0 0 1 3 4a1 1 0 0 1 1-1h3.5a1 1 0 0 1 1 1c0 1.25.2 2.45.57 3.57a1 1 0 0 1-.25 1z"/></svg>
      Phone: 9555 0148
    </p>
    <p class="contact-bar__hours">After Hours &amp; Saturday appointments available</p>
  </footer>
</main>
</body>
</html>
```